Flyer for Cutting Edge Professional Learning Organization for Education Leaders

We need a two page, eye catching flyer that grabs the attention of busy school and district education leaders. It will communicate the exciting professional learning experiences that we are offering during the next school year.

We have included our two page flyer from last year. As you'll see the second page is virtually all text, so very easy to design that.

You can replicate the format of last year's flyer (KL SEVIN 2016-17 Menu Final), making the various text changes and additions which we have included in our word document (KL SEVIN 2017-18 Programming Flyer). Or you can go with a new format. We are open to your creativity. We are also open to either a new image that communicates the concept of leadership or one that is similar to the one we used on the first page of last year's flyer.

Target Market(s)

School and district education leaders

Industry/Entity Type

Education

Contact Information for Business Card

Logo
Lo Wendell
Executive/Program Director
lo.wendell@mqtn.example
720-555-0148
4120 Quillmoor Road
Boulder, CO 80000

Font styles to use
Sans Serif

Colors
0255a3
ffffff
3176b5

Requirements
Must have
• My flyer must have the exact text which I have included on the Word document called KL SEVIN 2017-18 Programming Flyer. We do not have time to make lots of edits and corrections to text.
• Sharp, professional and creative look.
Should not have
• No spelling or punctuation errors.

```html
<!DOCTYPE html>
<html lang="en">
<head>
<meta charset="utf-8">
<title>KL SEVIN 2017-18 Programming Flyer</title>
<link href="https://fonts.googleapis.com/css2?family=Lato:ital,wght@0,400;0,700;0,900;1,700&display=swap" rel="stylesheet">
<style>
  :root {
    --cyan: #1fb6ef;
    --cyan-light: #5fd0f8;
    --cyan-deep: #0e9fdc;
    --navy: #0255a3;
    --header-dark: #232427;
    --header-mid: #4a4c50;
    --page-bg: #f3f4f6;
    --page-shade: #e7e9ec;
    --panel-bg: #ffffff;
    --body-text: #333333;
    --white: #ffffff;
  }
  * { box-sizing: border-box; margin: 0; padding: 0; }
  html, body { width: 923px; height: 1200px; overflow: hidden; }
  body {
    font-family: "Lato", Arial, sans-serif;
    background: var(--page-bg);
    color: var(--body-text);
    position: relative;
  }
  .page-texture {
    position: absolute; inset: 0;
    background:
      linear-gradient(135deg, transparent 0%, var(--page-shade) 22%, transparent 40%),
      linear-gradient(60deg, transparent 45%, var(--page-shade) 62%, transparent 80%),
      linear-gradient(160deg, var(--page-bg) 0%, #eceef1 50%, var(--page-bg) 100%);
    opacity: 0.8;
  }
  .site-banner {
    position: absolute; left: 0; top: 0; width: 923px; height: 86px;
    background:
      linear-gradient(115deg, transparent 30%, rgba(255,255,255,0.06) 48%, transparent 62%),
      linear-gradient(100deg, var(--header-dark) 0%, var(--header-mid) 40%, var(--header-dark) 72%, var(--header-mid) 100%);
    display: flex; align-items: center; justify-content: center;
  }
  .site-banner h1 {
    color: var(--white); font-weight: 900; font-size: 22.5px;
    text-transform: uppercase; letter-spacing: -0.3px;
  }
  .site-banner .url { color: var(--cyan); }

  .program-group {
    position: absolute; left: 60px; width: 803px;
    background: var(--panel-bg);
    border: 1.5px solid var(--cyan);
    border-radius: 12px;
    padding: 44px 16px 14px 14px;
  }
  .group-tab {
    position: absolute; left: 55px; width: 692px; top: -24px; height: 52px;
    border-radius: 10px;
    background: linear-gradient(90deg, var(--cyan-light) 0%, var(--cyan) 50%, var(--cyan-deep) 100%);
    display: flex; align-items: center; justify-content: center;
    color: var(--white); font-weight: 900; font-size: 22px; text-transform: uppercase;
    letter-spacing: 0.2px;
  }
  .program { margin-bottom: 13px; }
  .program:last-child { margin-bottom: 0; }
  .program h3 {
    color: var(--cyan-deep); font-weight: 900; font-size: 13px;
    text-transform: uppercase; margin-bottom: 1px;
  }
  .program p { font-size: 13.6px; line-height: 1.22; padding-right: 14px; }

  .testimonial {
    position: relative; margin: 14px 0 0 12px; padding: 4px 60px 0 48px;
    color: var(--cyan-deep); font-style: italic; font-weight: 700; font-size: 12.6px; line-height: 1.32;
  }
  .quote-mark {
    position: absolute; top: -8px; font-size: 70px; font-style: normal; font-weight: 900;
    color: var(--cyan); line-height: 1;
  }
  .quote-mark.open { left: 0; }
  .quote-mark.close { right: 22px; }

  .group-classroom { top: 126px; height: 210px; }
  .group-team { top: 382px; height: 222px; }
  .group-creative { top: 648px; height: 176px; }
  .group-pilot { top: 870px; height: 258px; }
</style>
</head>
<body>
  <div class="page-texture" role="img" aria-label="Faint light grey geometric background texture"></div>

  <header class="site-banner" role="banner">
    <h1>Go to <span class="url">klsevin.org</span> for session dates, details and facilitator bios</h1>
  </header>

  <section class="program-group group-classroom">
    <h2 class="group-tab">Shared Classroom Challenges</h2>
    <article class="program">
      <h3>K-12 and Preschool Instructional Rounds</h3>
      <p>Join other Metro Denver educators to hear diverse perspectives, challenge your thinking, and deepen your understanding of effective instruction and instructional leadership as you observe, discuss and reflect on key instructional challenges in K-12 and preschool classrooms.&nbsp; $30/session.</p>
    </article>
    <article class="program">
      <h3>Early Literacy Systems Learning Community</h3>
      <p>Discover how systems improvement frameworks can enhance the structures, processes and mindsets that impact early literacy results. Receive coaching and support from facilitators and learning community members as you use the frameworks to strengthen your early literacy results.&nbsp; No fee.</p>
    </article>
  </section>

  <section class="program-group group-team">
    <h2 class="group-tab">Team Leadership</h2>
    <article class="program">
      <h3>Feedback Fundamentals</h3>
      <p>Through hands-on collaborative sessions, you will learn about the art and science of feedback, from cultivating a coaching mindset to practical techniques for strengthening your delivery.&nbsp; Along the way, you will build lasting relationships with a cohort of peers from across metro Denver.&nbsp; Fee is $500.&nbsp; This year we are offering two additional, optional sessions focusing on feedback in the context of conflict and organizational change.&nbsp; Additional fee is $200.</p>
    </article>
    <article class="program">
      <h3>Leading Teams to the Top of Their Game</h3>
      <p>Connect with other Metro Denver education leaders as you generate new self-insights and gain powerful tools for more effective team leadership.&nbsp; This experience uses participants’ current team leadership challenges as the source for much of the cohort’s discussion.&nbsp; Fee is $500.</p>
    </article>
  </section>

  <section class="program-group group-creative">
    <h2 class="group-tab">Creative Solutions</h2>
    <article class="program">
      <h3>Design Thinking &amp; Creative Leadership</h3>
      <p>Our hallmark learning experiences!&nbsp; Draw upon your imagination, intuition, and creative reasoning to think differently about problems of practice in order to make positive change in classrooms, schools, and departments.&nbsp; Through this unique solution-building method and with coaching support, you will put your own creative leadership into action.&nbsp; Course fee is $150.</p>
    </article>
    <blockquote class="testimonial">
      <span class="quote-mark open" aria-hidden="true">“</span>
      The Design Thinking experience helped me see the great resources that surround me...my colleagues and all of our imaginations.
      <span class="quote-mark close" aria-hidden="true">”</span>
    </blockquote>
  </section>

  <section class="program-group group-pilot">
    <h2 class="group-tab">2017-18 Pilot Programs - No Fee for Pilot Participants</h2>
    <article class="program">
      <h3>Student-Driven Learning Hub</h3>
      <p>Design and pilot creative ways to help your staff foster student-driven learning environments.&nbsp; Build new relationships with local, regional and national peers as you experiment with new strategies and reflect on their effectiveness.</p>
    </article>
    <article class="program">
      <h3>Front Range Principals Club</h3>
      <p>Join principals from across the Front Range to discuss current education issues, exchange resources, and discover helpful leadership tools.&nbsp; Business leaders will be invited to some club events. Club members will determine the club’s specific activities.</p>
    </article>
    <article class="program">
      <h3>Opportunities for Highly Experienced Leaders</h3>
      <p>Work with other well-respected education leaders as you choose from an exciting menu of learning experiences that will help you elevate your leadership.&nbsp; Opportunities might include partnerships outside of education, stretch-to-learn experiences, and empathy experiences with students.</p>
    </article>
  </section>
</body>
</html>
```